First Breath Diving Kelp Dive Bonaire

Kelp Dive is looking for a great flyer to promote our First Breath Diving around Bonaire, the Caribbean.

Bonaire is shore dive capital of the world.
Our guests rent a pick-up truck. we would like to inform them about the possibilities of the First Breath Dive.

We have the logo, images and text available. Its the catchy and mind blowing design we are looking for to create an eye-catch flyer.
One side will be in English, the other side will be in Dutch.

Target Market(s)

Visitors (non divers) of the island Bonaire

Industry/Entity Type

Diving industry

Font styles to use
Sans Serif

Colors
0094D4
00A9DD
6FCCEA
C7EBF8
E9F6FB
F0912C
F2A743
F7CA91
FBE8D2
FDF5EE

Requirements
Must have
• The picture with the car and divers next to it is mandatory. Inspire to go for a first breath dive, show the beauty under water, easy to come dive with us, just takes half a day
Should not have
• Should not have pictures taken not around Bonaire.

```html
<!DOCTYPE html>
<html lang="nl">
<head>
<meta charset="utf-8">
<title>Kelp Dive – First Breath Diving on Bonaire, two sides</title>
<link href="https://fonts.googleapis.com/css2?family=Montserrat:wght@500;600;700;800&family=Poppins:wght@400;500&display=swap" rel="stylesheet">
<style>
  :root{
    --sky:#8fd6f4;
    --ocean-top:#1f9ccd;
    --ocean-mid:#1689bd;
    --ocean-deep:#0d5f93;
    --ring-soft:rgba(111,204,234,.6);
    --band:rgba(111,204,234,.45);
    --navy:#1c2c5e;
    --orange:#f2a743;
    --white:#ffffff;
    --paper:#e9f6fb;
  }
  *{box-sizing:border-box;margin:0;padding:0}
  html,body{width:764px;height:1200px;overflow:hidden;background:var(--paper)}
  .canvas{position:relative;width:764px;height:1200px}
  .sheet{position:absolute;left:182px;width:400px;height:566px;overflow:hidden}
  .sheet-nl{top:22px}
  .sheet-en{top:612px}
  .flyer{
    position:absolute;left:0;top:0;width:764px;height:1082px;overflow:hidden;
    transform:scale(0.5236);transform-origin:0 0;
    background:linear-gradient(180deg,var(--ocean-top) 0%,var(--ocean-mid) 45%,var(--ocean-deep) 100%);
    font-family:"Poppins",sans-serif;color:var(--white);
  }
  .hero{position:absolute;left:0;top:0;width:764px;height:420px}
  .brand{
    position:absolute;left:26px;top:20px;display:flex;align-items:center;gap:10px;
    font-family:"Montserrat",sans-serif;font-weight:800;font-size:30px;color:var(--navy);
  }
  .brand-dot{width:26px;height:26px;border-radius:50%;background:var(--orange)}
  .turtle{position:absolute;left:585px;top:372px;width:132px;height:100px;border-radius:50%;
    background:radial-gradient(ellipse at center,rgba(150,190,160,.55),rgba(31,156,205,0) 70%)}
  .photo-circle{position:absolute;border-radius:50%;border:7px solid var(--ring-soft)}
  .circle-gear{left:11px;top:411px;width:176px;height:176px;background:radial-gradient(circle at 50% 35%,#c9d8e0,#7d8f96 60%,#4c5a5e)}
  .circle-reef{left:138px;top:502px;width:160px;height:160px;background:radial-gradient(circle at 45% 45%,#4f8fc0,#2a6e9e 55%,#9a6a3a 100%)}
  .circle-fish{left:11px;top:571px;width:166px;height:166px;background:radial-gradient(circle at 50% 50%,#4a8298,#2f6a80 55%,#1d4d5f)}
  .headline{position:absolute;left:320px;top:462px;font-family:"Montserrat",sans-serif;font-weight:700;line-height:1}
  .headline span{display:block}
  .line-white{font-size:44px;color:var(--white);height:48px}
  .line-navy{font-size:44px;color:var(--navy);height:56px}
  .line-orange{font-size:66px;color:var(--orange);font-weight:800}
  .headline-nl{top:484px}
  .headline-nl .line-white{font-size:29px;height:36px}
  .headline-nl .line-navy{height:52px}
  .intro{position:absolute;left:322px;top:646px;width:380px;font-size:9.5px;line-height:1.25}
  .label{
    position:absolute;background:var(--orange);color:var(--white);
    font-family:"Montserrat",sans-serif;font-weight:600;font-size:12.5px;padding:2px 8px;
  }
  .label-passion{left:322px;top:708px}
  .label-paradise{left:26px;top:764px}
  .checklist{position:absolute;left:322px;top:738px;list-style:none;font-size:9.5px;line-height:20.4px}
  .checklist li{display:flex;align-items:center;gap:9px}
  .checklist svg{width:12px;height:10px;flex:none}
  .paradise-text{position:absolute;left:26px;top:792px;width:256px;font-size:9.5px;line-height:11.7px}
  .stop-by{position:absolute;left:28px;top:912px;width:706px;font-family:"Montserrat",sans-serif;font-weight:700;font-size:12.5px;line-height:1.3}
  .seabed{position:absolute;left:0;top:945px;width:764px;height:65px;
    background:radial-gradient(ellipse at 20% 100%,rgba(140,150,110,.5),rgba(0,0,0,0) 45%),radial-gradient(ellipse at 70% 110%,rgba(60,110,130,.5),rgba(0,0,0,0) 45%)}
  .contact-bar{position:absolute;left:0;top:1010px;width:764px;height:66px;background:var(--white);display:flex;align-items:center}
  .call-now{width:254px;height:100%;background:var(--navy);color:var(--orange);display:flex;align-items:center;justify-content:center;
    font-family:"Montserrat",sans-serif;font-weight:800;font-size:29px}
  .contact{display:flex;align-items:center;gap:5px;color:var(--navy);margin-left:16px}
  .contact svg{width:12px;height:12px;flex:none}
  .contact-phone{font-family:"Montserrat",sans-serif;font-weight:700;font-size:22px}
  .contact-small{font-size:10px}
  .bottom-strip{position:absolute;left:0;top:1076px;width:764px;height:6px;background:var(--ocean-deep)}
</style>
</head>
<body>
<div class="canvas">

  <!-- Dutch side -->
  <section class="sheet sheet-nl" lang="nl">
    <div class="flyer">
      <svg class="hero" viewBox="0 0 764 420">
        <defs>
          <linearGradient id="heroToneNl" x1="0" y1="0" x2="0" y2="1">
            <stop offset="0" stop-color="#8fd6f4"/><stop offset="0.35" stop-color="#3aa9d6"/>
            <stop offset="0.55" stop-color="#4bb5d8"/><stop offset="0.75" stop-color="#e6e3d8"/>
            <stop offset="1" stop-color="#d9d4c6"/>
          </linearGradient>
        </defs>
        <polygon points="0,295 331,394 764,361 764,383 331,416 0,317" fill="var(--band)"/>
        <polygon points="0,0 764,0 764,361 331,394 0,295" fill="url(#heroToneNl)" role="img" aria-label="Foto: twee duikers in wetsuit op een wit strand van Bonaire naast een witte pick-up met de zee erachter"/>
      </svg>
      <div class="brand"><span class="brand-dot"></span>Kelp Dive</div>
      <div class="turtle" role="img" aria-label="Illustratie van een zwemmende zeeschildpad"></div>
      <div class="photo-circle circle-gear" role="img" aria-label="Foto: duikuitrusting en maskers op een rots aan de kust"></div>
      <div class="photo-circle circle-reef" role="img" aria-label="Foto: kleurrijk koraalrif met vissen"></div>
      <div class="photo-circle circle-fish" role="img" aria-label="Foto: rifvis tussen waaierkoralen"></div>

      <h1 class="headline headline-nl">
        <span class="line-white">(FIRST BREATH DIVING)</span>
        <span class="line-navy">PROEFDUIK OP</span>
        <span class="line-orange">BONAIRE</span>
      </h1>
      <p class="intro">Word verliefd op het gevoel van duiken in een onderwaterparadijs. Onder begeleiding van een duikinstructeur ontdek je op een makkelijke en leuke manier alle basisvaardigheden voor een heerlijke duik.</p>

      <span class="label label-passion">LIEFDE VOOR HET WATERLEVEN</span>
      <ul class="checklist">
        <li><svg viewBox="0 0 12 10"><path d="M1 5l3.5 3.5L11 1" stroke="#f2a743" stroke-width="2" fill="none"/></svg>Onze proefduik is voor iedereen vanaf 10 jaar</li>
        <li><svg viewBox="0 0 12 10"><path d="M1 5l3.5 3.5L11 1" stroke="#f2a743" stroke-width="2" fill="none"/></svg>Na een korte theoretische introductie geniet je meteen van een duik</li>
        <li><svg viewBox="0 0 12 10"><path d="M1 5l3.5 3.5L11 1" stroke="#f2a743" stroke-width="2" fill="none"/></svg>De activiteit duurt 3 tot 4 uur</li>
        <li><svg viewBox="0 0 12 10"><path d="M1 5l3.5 3.5L11 1" stroke="#f2a743" stroke-width="2" fill="none"/></svg>Je kunt meedoen wanneer je gezond genoeg bent om jouw duikset te dragen</li>
        <li><svg viewBox="0 0 12 10"><path d="M1 5l3.5 3.5L11 1" stroke="#f2a743" stroke-width="2" fill="none"/></svg>Een groep bestaat uit maximaal 4 personen</li>
        <li><svg viewBox="0 0 12 10"><path d="M1 5l3.5 3.5L11 1" stroke="#f2a743" stroke-width="2" fill="none"/></svg>Hierdoor ervaar je de pracht van de oceaan zonder afleiding van anderen</li>
        <li><svg viewBox="0 0 12 10"><path d="M1 5l3.5 3.5L11 1" stroke="#f2a743" stroke-width="2" fill="none"/></svg>En heeft de duikinstructeur veel tijd voor persoonlijke aandacht</li>
      </ul>

      <span class="label label-paradise">ONDERWATERPARADIJS</span>
      <p class="paradise-text">Bonaire is bij uitstek de plek voor een proefduik. Na een korte introductie stappen we direct de zee in waar het rif al vrij snel begint. Bovendien kennen we de perfecte duikspots voor beginners. Hier loopt de zeebodem in een langzaam tempo naar beneden en word je verrast door de mooiste vissen en koralen.</p>

      <p class="stop-by">KOM GERUST LANGS BIJ ONZE FRONT-OFFICE. WIJ ZIJN GRAAG BEREID JE VRAGEN TE BEANTWOORDEN OF OM DE 'FIRST BREATH DIVE' IN TE PLANNEN.</p>
      <div class="seabed" role="img" aria-label="Foto: zachte koralen op de zeebodem"></div>

      <footer class="contact-bar">
        <div class="call-now">CALL US NOW</div>
        <div class="contact contact-phone">
          <svg viewBox="0 0 12 12"><path d="M2.5 1l2 2.5-1.2 1.2a7 7 0 0 0 4 4L8.5 7.5 11 9.5 9.8 11C5 11 1 7 1 2.2z" fill="#f2a743"/></svg>+(599) 555 01 23
        </div>
        <div class="contact contact-small">
          <svg viewBox="0 0 12 12"><rect x="1" y="2.5" width="10" height="7" fill="#f2a743"/><path d="M1 2.5l5 4 5-4" stroke="#fff" stroke-width="1" fill="none"/></svg>info@kelp-dive.com
        </div>
        <div class="contact contact-small">
          <svg viewBox="0 0 12 12"><circle cx="6" cy="6" r="5" fill="none" stroke="#f2a743" stroke-width="1.4"/><ellipse cx="6" cy="6" rx="2.2" ry="5" fill="none" stroke="#f2a743" stroke-width="1"/><path d="M1 6h10" stroke="#f2a743" stroke-width="1"/></svg>www.kelp-dive.com
        </div>
      </footer>
      <div class="bottom-strip"></div>
    </div>
  </section>

  <!-- English side -->
  <section class="sheet sheet-en" lang="en">
    <div class="flyer">
      <svg class="hero" viewBox="0 0 764 420">
        <defs>
          <linearGradient id="heroToneEn" x1="0" y1="0" x2="0" y2="1">
            <stop offset="0" stop-color="#8fd6f4"/><stop offset="0.35" stop-color="#3aa9d6"/>
            <stop offset="0.55" stop-color="#4bb5d8"/><stop offset="0.75" stop-color="#e6e3d8"/>
            <stop offset="1" stop-color="#d9d4c6"/>
          </linearGradient>
        </defs>
        <polygon points="0,295 331,394 764,361 764,383 331,416 0,317" fill="var(--band)"/>
        <polygon points="0,0 764,0 764,361 331,394 0,295" fill="url(#heroToneEn)" role="img" aria-label="Photo: two divers in wetsuits on a white Bonaire beach beside a white pick-up truck with the sea behind"/>
      </svg>
      <div class="brand"><span class="brand-dot"></span>Kelp Dive</div>
      <div class="turtle" role="img" aria-label="Illustration of a sea turtle swimming"></div>
      <div class="photo-circle circle-gear" role="img" aria-label="Photo: dive gear and masks laid out on a rock by the shore"></div>
      <div class="photo-circle circle-reef" role="img" aria-label="Photo: colourful coral reef with fish"></div>
      <div class="photo-circle circle-fish" role="img" aria-label="Photo: reef fish among sea fans and corals"></div>

      <h1 class="headline">
        <span class="line-white">FIRST BREATH</span>
        <span class="line-navy">DIVING ON</span>
        <span class="line-orange">BONAIRE</span>
      </h1>
      <p class="intro">Fall in love with diving in our underwater paradise. Under the guidance of a dive instructor you will learn the basic skills for peaceful diving in a fun and easy way</p>

      <span class="label label-passion">DEVELOP A PASSION FOR MARINE LIFE</span>
      <ul class="checklist">
        <li><svg viewBox="0 0 12 10"><path d="M1 5l3.5 3.5L11 1" stroke="#f2a743" stroke-width="2" fill="none"/></svg>Ages 10 and up can sign up for our first breath dive</li>
        <li><svg viewBox="0 0 12 10"><path d="M1 5l3.5 3.5L11 1" stroke="#f2a743" stroke-width="2" fill="none"/></svg>You'll dive straight into the water after a brief theoretic introduction</li>
        <li><svg viewBox="0 0 12 10"><path d="M1 5l3.5 3.5L11 1" stroke="#f2a743" stroke-width="2" fill="none"/></svg>The First Breath Diving course will take 3-4 hours</li>
        <li><svg viewBox="0 0 12 10"><path d="M1 5l3.5 3.5L11 1" stroke="#f2a743" stroke-width="2" fill="none"/></svg>Before participating, you are required to fill out a medical questionnaire</li>
        <li><svg viewBox="0 0 12 10"><path d="M1 5l3.5 3.5L11 1" stroke="#f2a743" stroke-width="2" fill="none"/></svg>A group consists of a maximum of 4 people</li>
        <li><svg viewBox="0 0 12 10"><path d="M1 5l3.5 3.5L11 1" stroke="#f2a743" stroke-width="2" fill="none"/></svg>Experience the splendor of the ocean without much distraction by other divers</li>
        <li><svg viewBox="0 0 12 10"><path d="M1 5l3.5 3.5L11 1" stroke="#f2a743" stroke-width="2" fill="none"/></svg>And enjoy a lot of personal attention given by your instructor</li>
      </ul>

      <span class="label label-paradise">UNDERWATER PARADISE</span>
      <p class="paradise-text">Bonaire is the place to learn how to scuba dive. After a brief introduction we will directly dive into the sea, where the reef starts in shallow waters. We know the perfect dive sites for beginners. Here, the sea bed slopes gradually down and you'll be amazed by the most beautiful fish and corals.</p>

      <p class="stop-by">STOP BY AT OUR FRONT OFFICE AND WE ARE HAPPY TO ANSWER ALL YOUR QUESTIONS OR TO BOOK</p>
      <div class="seabed" role="img" aria-label="Photo: soft coral heads on the sea floor"></div>

      <footer class="contact-bar">
        <div class="call-now">CALL US NOW</div>
        <div class="contact contact-phone">
          <svg viewBox="0 0 12 12"><path d="M2.5 1l2 2.5-1.2 1.2a7 7 0 0 0 4 4L8.5 7.5 11 9.5 9.8 11C5 11 1 7 1 2.2z" fill="#f2a743"/></svg>+(599) 555 01 23
        </div>
        <div class="contact contact-small">
          <svg viewBox="0 0 12 12"><rect x="1" y="2.5" width="10" height="7" fill="#f2a743"/><path d="M1 2.5l5 4 5-4" stroke="#fff" stroke-width="1" fill="none"/></svg>info@kelp-dive.com
        </div>
        <div class="contact contact-small">
          <svg viewBox="0 0 12 12"><circle cx="6" cy="6" r="5" fill="none" stroke="#f2a743" stroke-width="1.4"/><ellipse cx="6" cy="6" rx="2.2" ry="5" fill="none" stroke="#f2a743" stroke-width="1"/><path d="M1 6h10" stroke="#f2a743" stroke-width="1"/></svg>www.kelp-dive.com
        </div>
      </footer>
      <div class="bottom-strip"></div>
    </div>
  </section>

</div>
</body>
</html>
```